New Business Cards for KM&DR

We need updated business cards for a staff of 15 engineers, estimators, project managers, and sales people. We have recently begun changes to our website and marketing material to improve our look and branding. We are an established fabricator specializing in pressure vessels, tanks, and structural steel. The owners require us to use the existing logo and old english text design. Also, we prefer dark grey or mostly black cards.
Target Market(s)
Engineers, purchasing agents, estimators, and project managers of; mining companies, refineries, industrial construction professionals
Industry/Entity Type
Business
Contact Information for Business Card
Logo, phone, website, email, etc.
Look and feel
Each slider illustrates characteristics of the customer's brand and the style your logo design should communicate.

```html
<!DOCTYPE html>
<html lang="en">
<head>
<meta charset="utf-8">
<title>KM&amp;DR Business Card</title>
<link href="https://fonts.googleapis.com/css2?family=Open+Sans:wght@400;600&family=Tinos:ital,wght@0,400;0,700;1,400&display=swap" rel="stylesheet">
<style>
  :root {
    --canvas: #e9e7e4;
    --card: #000000;
    --ink: #ffffff;
    --line: #d9d9d9;
  }
  * { margin: 0; padding: 0; box-sizing: border-box; }
  html, body { width: 1200px; height: 900px; overflow: hidden; }
  body { background: var(--canvas); position: relative; font-family: "Open Sans", sans-serif; color: var(--ink); }
  .card { position: absolute; background: var(--card); width: 589px; height: 364px; }
  .card--front { left: 258px; top: 75px; }
  .card--back { left: 518px; top: 491px; }

  .badge { position: absolute; border: 2px solid var(--ink); }
  .badge--certified { left: 34px; top: 72px; width: 152px; height: 52px; border-radius: 26px; }
  .badge--stamp-a { left: 410px; top: 58px; width: 80px; height: 80px; border-radius: 8px; }
  .badge--stamp-b { left: 496px; top: 65px; width: 66px; height: 66px; border-radius: 6px; }

  .brand-mark { position: absolute; font-family: "Tinos", serif; font-weight: 700; color: var(--ink); text-align: center; letter-spacing: 1px; }
  .card--front .brand-mark { left: 229px; top: 68px; width: 130px; font-size: 24px; }
  .card--back .brand-mark { left: 0; top: 158px; width: 100%; font-size: 42px; }

  .company { position: absolute; left: 0; width: 100%; top: 168px; text-align: center; font-family: "Tinos", serif; }
  .company__name { display: inline-block; font-size: 21px; padding: 0 3px 2px; border-bottom: 1px solid var(--line); }
  .company__tagline { font-style: italic; font-size: 15px; margin-top: 3px; }

  .contact-person { position: absolute; right: 296px; top: 242px; text-align: right; }
  .contact-person__name { font-family: "Tinos", serif; font-weight: 700; font-size: 19px; line-height: 22px; }
  .contact-person__role, .contact-person__email { font-size: 14.5px; line-height: 22px; }
  .contact-person__email svg { vertical-align: -1px; margin-left: 5px; }

  .divider { position: absolute; left: 299px; top: 243px; width: 1px; height: 60px; background: var(--line); }

  .contact-lines { position: absolute; left: 315px; top: 241px; list-style: none; }
  .contact-lines li { font-size: 14.5px; line-height: 21.5px; display: flex; align-items: center; gap: 7px; }
  .contact-lines svg { flex: none; }

  .address { position: absolute; left: 0; width: 100%; top: 318px; text-align: center; font-size: 14.5px; }
</style>
</head>
<body>
  <section class="card card--front">
    <div class="badge badge--certified" aria-label="Certification badge"></div>
    <div class="brand-mark">KM&amp;DR</div>
    <div class="badge badge--stamp-a" aria-label="Accreditation badge"></div>
    <div class="badge badge--stamp-b" aria-label="Accreditation badge"></div>

    <div class="company">
      <div class="company__name">Kingsmill Metal &amp; Die Rolling</div>
      <div class="company__tagline">The Industrial Fabricator</div>
    </div>

    <div class="contact-person">
      <div class="contact-person__name">Daniel Harlow</div>
      <div class="contact-person__role">Managing Director</div>
      <div class="contact-person__email">info@kmanddr.com<svg width="11" height="9" viewBox="0 0 11 9"><rect x="0.5" y="0.5" width="10" height="8" fill="none" stroke="#fff"/><path d="M0.5 0.5 L5.5 5 L10.5 0.5" fill="none" stroke="#fff"/></svg></div>
    </div>

    <div class="divider"></div>

    <ul class="contact-lines">
      <li><svg width="13" height="11" viewBox="0 0 13 11"><path d="M1 3 Q6.5 -1 12 3 L10 4.5 L8.5 3 L4.5 3 L3 4.5 Z" fill="#fff"/><rect x="3" y="5" width="7" height="5" rx="1" fill="#fff"/></svg>801.555.0142</li>
      <li><svg width="13" height="12" viewBox="0 0 13 12"><rect x="0.5" y="3" width="12" height="8" rx="1" fill="#fff"/><rect x="3" y="0.5" width="7" height="3" fill="none" stroke="#fff"/><rect x="3" y="6" width="3" height="3" fill="#000"/></svg>801.555.0187</li>
      <li><svg width="13" height="13" viewBox="0 0 13 13"><circle cx="6.5" cy="6.5" r="5.5" fill="#fff"/><path d="M4 3 Q6 5 5 7 Q7 8 8 10 M8 2 Q9 4 10 4" fill="none" stroke="#000" stroke-width="1.2"/></svg>www.kmanddr.com</li>
    </ul>

    <div class="address">480 North 200, PO Box 320118, Riverton Falls, 84099</div>
  </section>

  <section class="card card--back">
    <div class="brand-mark">KM&amp;DR</div>
  </section>
</body>
</html>
```